Create for us a Shop-Stopper Business Card

We need a standout, first class business card to go along with our new brand strategy. Sleek, Contemporary and fresh.

Colors and theme must sync with our websitewww.pelvorpower.co.uk

We want a business card that has a global brand appeal. TKR Energy is a small UK renewable company that specialises in energy projects in Africa. We want a business card that has the following characteristics: Very short, precise, global, stand out, NOT TOO LOUD but contemporary. The company's colour themes are White, Grey with a hint of green.

Target Market(s)

Business exec, high net worth individuals, investors, commercial leaders, suppliers, government officials

Industry/Entity Type

Solar Energy

Contact Information for Business Card

Logo, Name, Title, Address, web address, email,

Requirements
Must have
• Logo must be sharp
Nice to have
• Adapt fonts from the logo. The large circular side of the logo at the back in a very refreshing way
Should not have
• No solar panel shapes or image.Very little black. If possible avoid black. Its not coming out nice. I think !!!

```html
<!DOCTYPE html>
<html lang="en">
<head>
<meta charset="utf-8">
<title>TKR Energy – Business Card</title>
<link href="https://fonts.googleapis.com/css2?family=Open+Sans:wght@400;600&display=swap" rel="stylesheet">
<style>
  :root {
    --backdrop: #5b4a3b;
    --card-white: #ffffff;
    --card-dark: #333333;
    --brand-green: #0f7a35;
    --brand-green-light: #7dc242;
    --text-grey: #3f3f3f;
    --band-dark: #333333;
  }
  * { margin: 0; padding: 0; box-sizing: border-box; }
  html, body {
    width: 1200px;
    height: 987px;
    overflow: hidden;
    background: var(--backdrop);
    font-family: "Open Sans", sans-serif;
  }
  .card {
    position: absolute;
    left: 293px;
    width: 615px;
    height: 352px;
    overflow: hidden;
  }
  .card--front { top: 130px; background: var(--card-white); }
  .card--back { top: 505px; background: var(--card-dark); }

  .brand {
    position: absolute;
    left: 55px;
    top: 146px;
    display: flex;
    align-items: center;
    gap: 10px;
  }
  .brand__dot {
    width: 48px;
    height: 48px;
    border-radius: 50%;
    background: var(--brand-green);
  }
  .brand__name {
    font-size: 32px;
    font-weight: 600;
    color: var(--text-grey);
    letter-spacing: 0.5px;
  }

  .contact {
    position: absolute;
    left: 352px;
    top: 88px;
    color: var(--text-grey);
    font-size: 16px;
    line-height: 23px;
  }
  .contact__name {
    font-size: 21px;
    font-weight: 600;
    color: var(--brand-green);
    line-height: 26px;
  }
  .contact__title { font-size: 16px; margin-bottom: 10px; }
  .contact__address { margin-bottom: 9px; }
  .contact__row { display: flex; align-items: center; gap: 8px; }
  .contact__row svg { width: 14px; height: 14px; flex: none; }

  .band {
    position: absolute;
    left: 0;
    top: 302px;
    width: 615px;
    height: 33px;
    background: var(--band-dark);
  }
  .band__green {
    position: absolute;
    left: 0;
    top: 0;
    width: 470px;
    height: 33px;
    background: linear-gradient(90deg, var(--brand-green) 0%, #2f9a3c 45%, var(--brand-green-light) 100%);
  }
  .band__url {
    position: absolute;
    left: 94px;
    top: 6px;
    font-size: 15px;
    letter-spacing: 3px;
    color: #ffffff;
  }
  .band__dot {
    position: absolute;
    left: 476px;
    top: -2px;
    width: 38px;
    height: 38px;
    border-radius: 50%;
    background: var(--brand-green);
    border: 3px solid #ffffff;
  }

  .back__dot {
    position: absolute;
    left: 397px;
    top: 211px;
    width: 112px;
    height: 112px;
    border-radius: 50%;
    background: var(--brand-green);
  }
</style>
</head>
<body>
  <section class="card card--front">
    <div class="brand">
      <span class="brand__dot"></span>
      <span class="brand__name">TKR ENERGY</span>
    </div>

    <div class="contact">
      <p class="contact__name">DANIEL REEVE</p>
      <p class="contact__title">CEO/FOUNDER</p>
      <p class="contact__address">4120 Larkspur Road<br>Fairbanks, Alaska 34918</p>
      <p class="contact__row">
        <svg viewBox="0 0 24 24" aria-hidden="true"><path fill="#0f7a35" d="M6.6 10.8a15.1 15.1 0 0 0 6.6 6.6l2.2-2.2a1 1 0 0 1 1-.25 11.4 11.4 0 0 0 3.6.6 1 1 0 0 1 1 1V20a1 1 0 0 1-1 1A17 17 0 0 1 3 4a1 1 0 0 1 1-1h3.5a1 1 0 0 1 1 1c0 1.25.2 2.45.6 3.6a1 1 0 0 1-.25 1z"/></svg>
        614 220 7391
      </p>
      <p class="contact__row">
        <svg viewBox="0 0 24 24" aria-hidden="true"><rect x="2" y="5" width="20" height="14" fill="#0f7a35"/><path d="M2 5l10 8 10-8" fill="none" stroke="#ffffff" stroke-width="2"/></svg>
        name@pelvorpower.co.uk
      </p>
    </div>

    <div class="band">
      <div class="band__green"></div>
      <span class="band__url">www.pelvorpower.co.uk</span>
      <span class="band__dot"></span>
    </div>
  </section>

  <section class="card card--back">
    <span class="back__dot"></span>
  </section>
</body>
</html>
```